Indy Film Production Company/Studio

We need a business card designed from an existing logo. We are a digital studio/production company that caters to creating genre entertainment, like Action, Horror, and martial arts. The card along with the logo will be used to Brand the company from letter heads to banners. The design will also be used for postcards and Brochures. It should be professional and masculine.
Updates

Thank you to all the designers who have participated. I'm narrowing down who it will be. Thank you again.

Target Market(s)

Investors, Networks, Producers, and actors

Industry/Entity Type

Film Production

Contact Information for Business Card

Benedikt Harwell
Producer/Writer/Director
www.copperlatchpictures.com

Requirements
Must have
• Website address, Facebook icon and Twitter icon possibly in the back of the card.
Nice to have
• Logline of Company: Follow The Action.

```html
<!DOCTYPE html>
<html lang="en">
<head>
<meta charset="utf-8">
<title>Copper Latch Pictures – Business Card</title>
<link rel="stylesheet" href="https://fonts.googleapis.com/css2?family=Montserrat:wght@400;500;700&display=swap">
<style>
  :root {
    --page: #2b2b2b;
    --card-black: #050505;
    --accent-red: #e8202a;
    --swoosh-white: #ffffff;
    --ink-light: #f2f2f2;
    --ink-silver: #d6d6d6;
    --icon-square: #4a4a4a;
  }
  * { box-sizing: border-box; margin: 0; padding: 0; }
  html, body {
    width: 1200px; height: 900px; overflow: hidden;
    background: var(--page);
    font-family: "Montserrat", Arial, sans-serif;
  }
  .canvas { position: relative; width: 1200px; height: 900px; }
  .card {
    position: absolute; width: 735px; height: 420px;
    background: var(--card-black);
    overflow: hidden;
    box-shadow: 0 14px 30px rgba(0,0,0,.55);
  }
  .card--front { left: 60px; top: 30px; }
  .card--back { left: 405px; top: 465px; }
  .card__swoosh { position: absolute; inset: 0; width: 100%; height: 100%; }

  .wordmark {
    position: absolute;
    color: var(--ink-silver);
    font-weight: 700;
    text-transform: uppercase;
    letter-spacing: 2px;
    line-height: 1.1;
    text-align: center;
    white-space: nowrap;
  }
  .card--front .wordmark { left: 170px; top: 140px; width: 380px; font-size: 34px; }
  .card--back .wordmark { left: 150px; top: 280px; width: 380px; font-size: 32px; }

  .web {
    position: absolute; right: 60px; bottom: 115px;
    font-size: 17px; color: var(--ink-light); letter-spacing: .3px;
    white-space: nowrap;
  }
  .web__domain { color: var(--accent-red); }

  .social { position: absolute; left: 40px; bottom: 36px; display: flex; gap: 22px; }
  .social__square { width: 40px; height: 40px; border-radius: 6px; background: var(--icon-square); }

  .contact {
    position: absolute; right: 150px; top: 48px;
    text-align: right; color: var(--ink-light);
  }
  .contact__name {
    font-size: 21px; font-weight: 500; color: var(--accent-red);
    letter-spacing: 1.5px; text-transform: uppercase;
  }
  .contact__role { font-size: 14px; letter-spacing: 1px; margin-bottom: 22px; margin-top: 2px; }
  .contact__line { font-size: 15px; line-height: 22px; display: flex; justify-content: flex-end; align-items: center; gap: 8px; }
  .contact__icon { width: 12px; height: 12px; flex: none; }
</style>
</head>
<body>
<main class="canvas">

  <section class="card card--front" aria-label="Card front">
    <svg class="card__swoosh" viewBox="0 0 735 420" aria-hidden="true">
      <path d="M190 0 H735 V170 Z" fill="var(--accent-red)"/>
      <path d="M0 0 H190 C400 20 630 90 735 160 V420 H0 Z" fill="var(--swoosh-white)"/>
      <path d="M0 0 H230 C420 40 620 110 735 200 V420 H0 Z" fill="var(--card-black)"/>
    </svg>
    <div class="wordmark">Copper Latch<br>Pictures</div>
    <p class="web">www.<span class="web__domain">copperlatchpictures</span>.com</p>
    <div class="social">
      <span class="social__square"></span>
      <span class="social__square"></span>
    </div>
  </section>

  <section class="card card--back" aria-label="Card back">
    <svg class="card__swoosh" viewBox="0 0 735 420" aria-hidden="true">
      <path d="M600 0 H735 V420 H470 Z" fill="var(--accent-red)"/>
      <ellipse cx="110" cy="260" rx="665" ry="430" fill="var(--swoosh-white)"/>
      <ellipse cx="90" cy="250" rx="660" ry="430" fill="var(--card-black)"/>
    </svg>
    <div class="contact">
      <p class="contact__name">Benedikt Harwell</p>
      <p class="contact__role">DIRECTOR</p>
      <p class="contact__line">+330 2460-7314
        <svg class="contact__icon" viewBox="0 0 12 12"><path d="M2 1 L4.5 1 L5.5 3.5 L4 4.8 Q5.2 7 7.2 8 L8.5 6.5 L11 7.5 L11 10 Q6 11 1 3 Z" fill="var(--accent-red)"/></svg>
      </p>
      <p class="contact__line">info@copperlatchpictures.com
        <svg class="contact__icon" viewBox="0 0 12 12"><rect x="1" y="2.5" width="10" height="7" rx="1" fill="var(--accent-red)"/><path d="M1.5 3 L6 6.5 L10.5 3" stroke="var(--card-black)" fill="none"/></svg>
      </p>
      <p class="contact__line">www.copperlatchpictures.com
        <svg class="contact__icon" viewBox="0 0 12 12"><circle cx="6" cy="6" r="5" fill="var(--accent-red)"/><path d="M1 6 H11 M6 1 Q3 6 6 11 M6 1 Q9 6 6 11" stroke="var(--card-black)" stroke-width=".8" fill="none"/></svg>
      </p>
    </div>
    <div class="wordmark">Copper Latch<br>Pictures</div>
  </section>

</main>
</body>
</html>
```